Bespoke Builders Business Card Design

We need a business card for an established builder of high quality bespoke homes in Auckland and Northland. We build and renovate homes collaboratively facilitating effective communication between owners, builders, architects, suppliers and tradespeople. We have never built or renovated a home that leaks or has faults. We only use reliable materials. We have never been sued or had legal action taken against us. We are honest builders of bespoke homes not group mass produced homes. Our niche market is in character homes. We practice sustainability and have built a lot of coastal property. We have been in business for over thirty years . We would like to see natural colors of the environment sand,sea and maybe vegetation . The design should communicate quality, sustainability,fair pricing, open communication and the originality of bespoke building. And the fact that the builder is registered.

Business

Rowan Tillery Builders
Ph. 027318592
18 Garnet Rd Ferndale Bay Auckland 0814
PO Box 958 Mangawhai 0371

```html
<!DOCTYPE html>
<html lang="en">
<head>
<meta charset="utf-8">
<title>Rowan Tillery Builders – Business Card</title>
<link rel="stylesheet" href="https://fonts.googleapis.com/css2?family=Open+Sans:wght@400&family=Tinos&display=swap">
<style>
  :root {
    --sand: #d9c9a6;
    --sand-light: #f7f2e8;
    --card-white: #ffffff;
    --sea: #1d5f8a;
    --sea-bright: #3f8fbf;
    --vegetation: #4e6b3a;
    --card-deep: #0a1014;
    --card-deep-sheen: #1b2327;
    --ink: #1f2326;
  }
  html, body {
    margin: 0;
    padding: 0;
    width: 1200px;
    height: 892px;
    overflow: hidden;
    background: var(--sand);
  }
  .canvas {
    position: relative;
    width: 1200px;
    height: 892px;
  }
  .card {
    position: absolute;
    left: 250px;
    width: 700px;
    height: 400px;
    box-shadow: 0 6px 18px rgba(60, 45, 20, 0.3);
    overflow: hidden;
  }
  .card--front {
    top: 30px;
    background: radial-gradient(ellipse at 40% 45%, var(--card-white) 55%, var(--sand-light) 100%);
  }
  .card--back {
    top: 462px;
    background: linear-gradient(135deg, var(--card-deep) 0%, var(--card-deep-sheen) 55%, var(--card-deep) 100%);
  }
  .front__name {
    position: absolute;
    left: 42px;
    top: 62px;
    margin: 0;
    font-family: "Open Sans", sans-serif;
    font-weight: 400;
    font-size: 46px;
    line-height: 62px;
    color: var(--sea);
    letter-spacing: 0.3px;
  }
  .front__divider {
    position: absolute;
    left: 0;
    right: 0;
    top: 168px;
    height: 2px;
    background: var(--vegetation);
  }
  .front__contact {
    position: absolute;
    right: 38px;
    top: 200px;
    margin: 0;
    padding: 0;
    list-style: none;
    font-family: "Open Sans", sans-serif;
    font-weight: 400;
    font-size: 21px;
    color: var(--ink);
    line-height: 34px;
  }
  .contact__line {
    display: flex;
    justify-content: flex-end;
    align-items: center;
    gap: 18px;
    white-space: nowrap;
  }
  .contact__line--plain { padding-right: 34px; }
  .contact__phones { word-spacing: 18px; }
  .contact__icon {
    width: 16px;
    height: 16px;
    flex: none;
  }
  .back__name {
    position: absolute;
    left: 0;
    right: 0;
    top: 168px;
    margin: 0;
    text-align: center;
    font-family: "Tinos", serif;
    font-weight: 400;
    font-size: 50px;
    line-height: 64px;
    color: var(--sea-bright);
  }
</style>
</head>
<body>
<main class="canvas">
  <section class="card card--front" aria-label="Card front">
    <h1 class="front__name">Rowan Tillery Builders</h1>
    <div class="front__divider"></div>
    <ul class="front__contact">
      <li class="contact__line">
        <span class="contact__phones">0461823507 027318592</span>
        <svg class="contact__icon" viewBox="0 0 16 16" aria-hidden="true">
          <rect width="16" height="16" fill="var(--sea)"/>
          <path d="M5 4 L7 4 L7.5 6 L6.5 7 Q7.5 9 9 9.5 L10 8.5 L12 9 L12 11 Q8 12 5 8 Q4 6 5 4 Z" fill="#fff"/>
        </svg>
      </li>
      <li class="contact__line">
        <span>18 Garnet Rd Ferndale Bay Auckland 0814</span>
        <svg class="contact__icon" viewBox="0 0 16 16" aria-hidden="true">
          <rect width="16" height="16" fill="var(--sea)"/>
          <path d="M3.5 8 L8 4 L12.5 8 L11 8 L11 12 L5 12 L5 8 Z" fill="#fff"/>
        </svg>
      </li>
      <li class="contact__line contact__line--plain">
        <span>PO Box 958 Mangawhai 0371</span>
      </li>
    </ul>
  </section>

  <section class="card card--back" aria-label="Card back">
    <h2 class="back__name">Rowan Tillery Builders</h2>
  </section>
</main>
</body>
</html>
```